Varden Chiropractic Business Cards

[Front]
[FLX/Stonerunner LOGO & Varden Chiropractic LOGO]
Neck & Back Pain Relief
Dr. Marcus Varden
Doctor of Chiropractic

• Short Term Care For Your Neck & Back Pain
• No Referral Needed
• Affordable / Insurance Accepted
• Proficient in treating Soft Tissue Problems

[Back]
For Valuable Wellness Inbox Notes™ Emailed To You Free, Go To:
www.DrMarcusVardenJournal.example
[SpinaGuard LOGO] - can be small

OFFICE HOURS:
Monday – Thursday
9 am - 12 noon, 2 pm - 6 pm
WALK-INS WELCOME

Industry/Entity Type

Business

Contact Information for Business Card

Varden Chiropractic Center, PLLC
4387 Talbrook Avenue, Suite H
New Bern, NC 28560
(252) 555-0147
www.vardenchiro.example

Requirements
Must have
• The FLX/Stonerunner Logo
The Varden Chiropractic Logo
Should not have
• A picture of a spine

```html
<!DOCTYPE html>
<html lang="en">
<head>
<meta charset="utf-8">
<title>Varden Chiropractic Business Card</title>
<link rel="stylesheet" href="https://fonts.googleapis.com/css2?family=Source+Sans+3:wght@400;600;700&display=swap">
<style>
  :root {
    --backdrop: #7a5a3c;
    --paper: #ffffff;
    --slate: #46596f;
    --slate-deep: #3d4f64;
    --wave-blue: #1ca4dc;
    --wave-pale: #7fcdee;
    --navy: #1f3550;
    --ink-light: #ffffff;
    --badge-red: #c8202f;
    --badge-blue: #1d4f9c;
    --rule: #c9d2dc;
  }
  * { box-sizing: border-box; margin: 0; padding: 0; }
  html, body {
    width: 996px; height: 1200px; overflow: hidden;
    background: var(--backdrop);
    font-family: "Source Sans 3", "Myriad Pro", Arial, sans-serif;
  }
  .card {
    position: absolute; left: 104px; width: 786px; height: 448px;
    overflow: hidden; box-shadow: 0 4px 14px rgba(0,0,0,.35);
  }
  .card--front { top: 134px; background: var(--slate); }
  .card--back { top: 603px; background: var(--slate-deep); color: var(--ink-light); }

  /* front */
  .front-top { position: absolute; inset: 0; }
  .brand-row {
    position: absolute; top: 64px; left: 0; width: 100%;
    display: flex; align-items: center; justify-content: center; gap: 28px;
  }
  .brand-name {
    color: var(--navy); font-weight: 400; font-size: 33px;
    letter-spacing: 1.5px; text-transform: uppercase; line-height: 1;
  }
  .brand-mark { width: 22px; height: 22px; border-radius: 50%; background: var(--wave-blue); }
  .brand-lockup { display: flex; align-items: center; gap: 12px; }
  .partner-badges { display: flex; align-items: center; gap: 14px; margin-left: 10px; }
  .partner-badge--flx { width: 104px; height: 30px; border-radius: 15px; background: var(--badge-red); }
  .partner-divider { width: 1px; height: 34px; background: var(--rule); }
  .partner-badge--stone { width: 110px; height: 26px; background: var(--badge-blue); }
  .tagline {
    position: absolute; top: 150px; width: 100%; text-align: center;
    color: var(--navy); font-size: 32px; font-weight: 400; letter-spacing: .5px;
    line-height: 38px; text-transform: uppercase;
  }
  .doctor {
    position: absolute; top: 266px; width: 100%; text-align: center;
    color: var(--ink-light); font-size: 26px; font-weight: 400;
  }
  .doctor strong { font-weight: 700; }
  .practice {
    position: absolute; top: 312px; right: 477px; text-align: right; font-style: normal;
    color: var(--ink-light); font-size: 20px; line-height: 28px;
  }
  .practice .practice-name { font-weight: 700; }
  .practice .phone {
    margin-top: 6px; display: flex; justify-content: flex-end; align-items: center; gap: 8px;
  }
  .phone svg { width: 14px; height: 20px; }
  .divider { position: absolute; top: 310px; left: 320px; width: 1px; height: 128px; background: var(--rule); }
  .benefits {
    position: absolute; top: 310px; left: 330px; list-style: none;
    color: var(--ink-light); font-size: 20px; line-height: 28.5px;
  }
  .benefits li::before { content: "• "; }

  /* back */
  .promo { position: absolute; top: 30px; left: 44px; font-size: 21px; line-height: 38px; }
  .promo .url { font-weight: 700; font-size: 23px; }
  .seal {
    position: absolute; top: 160px; left: 44px;
    display: flex; align-items: center; gap: 10px;
  }
  .seal-mark { width: 22px; height: 22px; background: var(--ink-light); }
  .seal-name { font-size: 32px; font-weight: 600; }
  .hours { position: absolute; top: 262px; left: 40px; font-size: 21px; line-height: 31px; }
  .hours h2 { font-size: 24px; font-weight: 700; line-height: 26px; }
  .walk-ins { position: absolute; top: 380px; left: 40px; font-size: 25px; text-transform: uppercase; }
  .back-lockup {
    position: absolute; top: 150px; left: 470px; width: 260px; height: 150px;
    display: flex; flex-direction: column; align-items: center; justify-content: center; gap: 14px;
  }
  .back-lockup .brand-mark { width: 40px; height: 40px; }
  .back-lockup .brand-name { color: var(--wave-pale); font-size: 30px; text-align: center; line-height: 1.15; }
</style>
</head>
<body>
  <section class="card card--front" aria-label="Business card front">
    <svg class="front-top" viewBox="0 0 786 448" preserveAspectRatio="none" aria-hidden="true">
      <path d="M0 0 H786 V200 C640 204 470 212 330 230 C220 244 90 232 0 206 Z" fill="var(--paper)"/>
      <path d="M0 206 C90 232 220 244 330 230 C470 212 640 204 786 200 L786 208 C640 212 470 220 330 238 C220 252 90 240 0 214 Z" fill="var(--wave-blue)"/>
      <path d="M0 220 C90 246 220 258 340 244 C480 226 640 216 786 214 L786 218 C640 220 480 230 340 248 C220 262 90 250 0 224 Z" fill="var(--wave-pale)"/>
    </svg>

    <div class="brand-row">
      <div class="brand-lockup">
        <span class="brand-mark" aria-hidden="true"></span>
        <span class="brand-name">Varden Chiropractic</span>
      </div>
      <div class="partner-badges" aria-label="FLX / Stonerunner partner badges">
        <span class="partner-badge--flx"></span>
        <span class="partner-divider"></span>
        <span class="partner-badge--stone"></span>
      </div>
    </div>
    <h1 class="tagline">Neck &amp; Back Pain Relief</h1>

    <p class="doctor"><strong>Dr. Marcus Varden,</strong> Doctor of Chiropractic</p>

    <address class="practice">
      <div class="practice-name">Varden Chiropractic Center</div>
      <div>PLLC 4387 Talbrook Avenue</div>
      <div>Suite H New Bern, NC 28560</div>
      <div class="phone">
        <svg viewBox="0 0 14 20" aria-hidden="true"><path d="M4 1 L7 1 L7 6 L5 7 C5 10 5 12 5 13 L7 14 L7 19 L4 19 C1 16 1 4 4 1 Z" fill="var(--ink-light)"/></svg>
        <span>(252) 555-0147</span>
      </div>
    </address>

    <span class="divider" aria-hidden="true"></span>
    <ul class="benefits">
      <li>Short Term Care For Your Neck &amp; Back Pain</li>
      <li>No Referral Needed</li>
      <li>Affordable / Insurance Accepted</li>
      <li>Proficient in treating Soft Tissue Problems</li>
    </ul>
  </section>

  <section class="card card--back" aria-label="Business card back">
    <div class="promo">
      <p>For Valuable Wellness Inbox Notes™</p>
      <p>Emailed To You Free, Go To:</p>
      <p class="url">www.DrMarcusVardenJournal.example</p>
    </div>
    <div class="seal">
      <span class="seal-mark" aria-hidden="true"></span>
      <span class="seal-name">SpinaGuard</span>
    </div>
    <div class="hours">
      <h2>OFFICE HOURS:</h2>
      <p>Monday – Thursday:</p>
      <p>9 am - 12 noon, 2 pm - 6 pm</p>
    </div>
    <p class="walk-ins">Walk-ins Welcome</p>
    <div class="back-lockup">
      <span class="brand-mark" aria-hidden="true"></span>
      <span class="brand-name">Varden<br>Chiropractic</span>
    </div>
  </section>
</body>
</html>
```